Trondel Group letterhead

Hi,

I need a letterhead template created for our business. This should be done in word format and A4 size. The images need to not move in the template ie when I am adding writing in etc. and should flow on when I get to a second page.

I have attached our logo templates below.

Other details to include on the letterhead somewhere are:

0438 571 962
Max@Trondelelectrical.example.com.au
PO Box 781 Marrowdale NSW 2163
ABN: 57 318 492 076

Thanks!

```html
<!DOCTYPE html>
<html lang="en">
<head>
<meta charset="utf-8">
<title>Trondel Group Letterhead</title>
<link href="https://fonts.googleapis.com/css2?family=Montserrat:wght@400;500;700&display=swap" rel="stylesheet">
<style>
  :root {
    --backdrop: #d3d3d3;
    --paper: #ffffff;
    --ink: #2a2a2a;
    --accent: #f26a1b;
    --watermark: #e8e8e8;
    --rule: #333333;
  }
  * { margin: 0; padding: 0; box-sizing: border-box; }
  html, body {
    width: 1200px; height: 903px; overflow: hidden;
    background: var(--backdrop);
    font-family: "Montserrat", sans-serif;
    color: var(--ink);
  }
  .canvas { position: relative; width: 1200px; height: 903px; }
  .sheet {
    position: absolute; top: 144px;
    width: 435px; height: 614px;
    background: var(--paper);
    box-shadow: 0 1px 3px rgba(0,0,0,0.25);
  }
  .sheet--first { left: 139px; }
  .sheet--second { left: 625px; }
  .sheet-label {
    position: absolute; top: 788px; width: 200px;
    text-align: center; font-size: 10.5px; letter-spacing: 1.2px;
    color: var(--ink);
  }
  .sheet-label--first { left: 256px; }
  .sheet-label--second { left: 744px; }

  .contact-list {
    position: absolute; left: 28px; top: 52px;
    list-style: none; font-size: 7.6px; line-height: 10px;
  }
  .contact-list li { display: flex; align-items: center; gap: 5px; }
  .contact-list svg { width: 7px; height: 7px; flex: none; }

  .postal {
    position: absolute; right: 27px; top: 52px;
    text-align: right; font-size: 7.6px; line-height: 10px;
    font-style: normal;
  }

  .brand-mark {
    position: absolute; left: 199px; top: 34px;
    width: 36px; height: 36px;
  }
  .header-rule {
    position: absolute; left: 28px; right: 28px; top: 90px;
    height: 0; border-top: 0.8px solid var(--rule);
  }
  .brand-name {
    position: absolute; left: 0; right: 0; top: 84px;
    text-align: center;
  }
  .brand-name span {
    display: inline-block; background: var(--paper);
    padding: 0 7px; font-size: 10px; font-weight: 700;
    letter-spacing: 0.8px; text-transform: uppercase;
    color: var(--ink); line-height: 12px;
  }

  .watermark {
    position: absolute; left: 75px; top: 185px;
    width: 286px; height: 286px;
  }
  .watermark-name {
    position: absolute; left: 75px; top: 185px;
    width: 286px; height: 286px;
    display: flex; align-items: center; justify-content: center;
    font-size: 38px; font-weight: 700; letter-spacing: 1px;
    color: var(--watermark); text-transform: uppercase;
  }
</style>
</head>
<body>
<div class="canvas">

  <section class="sheet sheet--first" aria-label="Letterhead first page">
    <ul class="contact-list">
      <li>
        <svg viewBox="0 0 10 10" aria-hidden="true"><path d="M2 1 L3.6 1 L4.3 3 L3.2 3.8 Q4 5.8 6.2 6.8 L7 5.7 L9 6.4 L9 8 Q8.6 9 7.5 9 Q1 8.4 1 2.4 Q1 1 2 1 Z" fill="var(--accent)"/></svg>
        0438 571 962
      </li>
      <li>
        <svg viewBox="0 0 10 10" aria-hidden="true"><rect x="0.5" y="2" width="9" height="6.5" fill="var(--accent)"/><path d="M0.8 2.3 L5 5.6 L9.2 2.3" stroke="#fff" stroke-width="0.9" fill="none"/></svg>
        Max@Trondelelectrical.example.com.au
      </li>
      <li>
        <svg viewBox="0 0 10 10" aria-hidden="true"><circle cx="5" cy="5" r="4.2" fill="var(--accent)"/><path d="M1 5 H9 M5 0.8 Q2.6 5 5 9.2 M5 0.8 Q7.4 5 5 9.2" stroke="#fff" stroke-width="0.7" fill="none"/></svg>
        Trondelelectrical.example.com.au
      </li>
    </ul>

    <svg class="brand-mark" viewBox="0 0 36 36" aria-hidden="true">
      <circle cx="18" cy="18" r="16" fill="none" stroke="var(--ink)" stroke-width="3"/>
    </svg>
    <div class="header-rule"></div>
    <div class="brand-name"><span>Trondel Group</span></div>

    <address class="postal">
      PO Box 781<br>
      Marrowdale, NSW 2163<br>
      ABN: 57 318 492 076
    </address>

    <svg class="watermark" viewBox="0 0 286 286" aria-hidden="true">
      <circle cx="143" cy="143" r="133" fill="none" stroke="var(--watermark)" stroke-width="20"/>
    </svg>
    <div class="watermark-name">Trondel</div>
  </section>

  <section class="sheet sheet--second" aria-label="Letterhead continuation page">
    <svg class="watermark" viewBox="0 0 286 286" aria-hidden="true">
      <circle cx="143" cy="143" r="133" fill="none" stroke="var(--watermark)" stroke-width="20"/>
    </svg>
    <div class="watermark-name">Trondel</div>
  </section>

  <p class="sheet-label sheet-label--first">PAGE 01</p>
  <p class="sheet-label sheet-label--second">PAGE 02</p>

</div>
</body>
</html>
```